BROCHURE OR FLYER PLEASE

We need a brochure design for our company TV Surfacing Contractors Limited. Our website is www.tvsurfacing-demo.co.nz. We have rented a 3m permanent booth at the dwelling plans hub in central Auckland. Their website is: www.dwellingplans-demo.co.nz
We need to design and provide a company brochure outlining who we are, and the types of services we provide. Half of our flooring business is dedicated to basically Polished Concrete/Concrete Grinding; and the other half to resin and other floor toppings. We are based in Auckland, NZ and will be marketing to existing and new home owners essentially in Auckland. We want to contain concise information on our services and present this in a professional but sheik style. Housing in NZ is expensive so our brochure needs to be up market and user friendly. Polished concrete is more expensive that carpet so I feel it is important to list the benefits etc. I will attach our website and information regarding our products. We would like a double sided brochure. Our company colours are blue/red/black. I have attached some photo's you are welcome to use. Please refer to our website for more information www.tvsurfacing-demo.co.nz. Thank you.

Target Market(s)

Home Owners

Industry/Entity Type

Marketing

Requirements
Must have
• Company logo and contact details.

```html
<!DOCTYPE html>
<html lang="en">
<head>
<meta charset="utf-8">
<title>TV Surfacing Contractors – Services Brochure (Inside Spread)</title>
<link href="https://fonts.googleapis.com/css2?family=Roboto:wght@300;400&display=swap" rel="stylesheet">
<style>
  :root {
    --sky: #29abe2;
    --sky-soft: rgba(41, 171, 226, 0.82);
    --sky-pale: #bfe6f7;
    --ink: #3c4a52;
    --paper: #ffffff;
    --stage: #f2f4f5;
    --stone: #4d5a58;
    --timber: #a8672a;
  }
  html, body {
    margin: 0;
    padding: 0;
    width: 1200px;
    height: 1000px;
    overflow: hidden;
    background: var(--stage);
    font-family: "Roboto", Arial, sans-serif;
  }
  .spread {
    position: absolute;
    left: 90px;
    top: 140px;
    width: 1020px;
    height: 720px;
    display: flex;
    box-shadow: 0 10px 30px rgba(0,0,0,0.12);
  }
  .panel {
    position: relative;
    width: 340px;
    height: 720px;
    background: var(--paper);
    overflow: hidden;
  }
  .panel + .panel { border-left: 1px solid #e4e8ea; }

  .heading {
    font-weight: 300;
    text-transform: uppercase;
    color: var(--sky);
    line-height: 1.02;
    margin: 0;
  }
  .body-copy {
    font-size: 10.5px;
    line-height: 1.35;
    color: var(--ink);
    margin: 0 0 10px;
  }
  .photo { position: absolute; }

  /* Left panel */
  .block-honing { position: absolute; left: 22px; top: 26px; right: 22px; }
  .block-honing .heading { font-size: 27px; }
  .block-honing .subhead { font-size: 15px; font-weight: 300; color: var(--sky); text-transform: uppercase; margin: 2px 0 8px; }
  .block-honing .body-copy { color: var(--sky); }
  .grinding-box {
    position: absolute; left: 0; top: 205px; width: 320px; height: 260px;
    background: var(--sky); color: var(--paper); padding: 22px 20px; box-sizing: border-box;
  }
  .grinding-box .heading { color: var(--paper); font-size: 25px; margin-bottom: 10px; }
  .grinding-box .lead { font-size: 11.5px; margin: 0 0 12px 6px; }
  .grinding-box .body-copy { color: var(--paper); font-size: 11.5px; }
  .house-photo {
    left: 0; top: 465px; width: 340px; height: 255px;
    background: linear-gradient(180deg, #e6eef2 0%, #dfe5e6 45%, #6f7b5e 70%, #c9c5bc 100%);
  }

  /* Middle panel */
  .non-slip { position: absolute; left: 22px; top: 28px; right: 22px; }
  .non-slip .heading { font-size: 27px; margin-bottom: 18px; }
  .options { margin: 0; padding-left: 16px; font-size: 10.5px; line-height: 1.35; color: var(--ink); }
  .options li { margin-bottom: 2px; }
  .pool-photo {
    left: 140px; top: 585px; width: 200px; height: 135px;
    background: linear-gradient(180deg, #9fdcf4 0%, #5bbde6 55%, #1f8fd0 100%);
  }

  /* Right panel */
  .floor-photo {
    inset: 0;
    background: linear-gradient(160deg, #7b4a1f 0%, var(--timber) 18%, #5b6462 40%, var(--stone) 70%, #3c4644 100%);
  }
  .resin-title-band {
    position: absolute; left: 0; top: 0; width: 250px; height: 130px;
    background: var(--sky-pale); opacity: 0.92;
  }
  .resin-title-band .heading { position: absolute; left: 30px; top: 42px; font-size: 27px; color: #ffffff; text-shadow: 0 0 1px rgba(41,171,226,.6); }
  .resin-box {
    position: absolute; left: 0; top: 130px; width: 310px; height: 360px;
    background: var(--sky-soft); padding: 18px 20px; box-sizing: border-box;
  }
  .resin-box .body-copy { color: var(--paper); font-size: 10.5px; }
</style>
</head>
<body>
<main class="spread">

  <section class="panel panel-left">
    <div class="block-honing">
      <h2 class="heading">Block Honing</h2>
      <p class="subhead">(Verticle Block Grinding)</p>
      <p class="body-copy">Block honing of concrete walls is a great way to achieve unique, appealing feature in your home or workplace. It creates a smooth, glossy finish which is similar to marble or terrazzo.</p>
    </div>
    <div class="grinding-box">
      <h2 class="heading">Concrete Grinding</h2>
      <p class="lead">Preparation for Carpet and Tiles:</p>
      <p class="body-copy">If you are looking to put carpet or tiles on your existing concrete floors, it is important to have them sufficiently prepared first in order to achieve a good result. Concrete preparation (also known as concrete resurfacing) is one of our specialities, so you can count on a high quality job.</p>
    </div>
    <div class="photo house-photo" role="img" aria-label="Modern white house with a covered patio, outdoor furniture and a polished concrete terrace"></div>
  </section>

  <section class="panel panel-middle">
    <div class="non-slip">
      <h2 class="heading">Non-Slip<br>Coatings and<br>Applications</h2>
      <p class="body-copy">If you have an area in your property that requires a non-slip surface (such as a walkways, patio areas, garages, carports, bathrooms or pool surroundings etc) talk to us at TV Surfacing Contractors.</p>
      <p class="body-copy">Our concrete systems and non-slip applications are ideal for a number of requirements, and will leave your concrete floors looking great!</p>
      <p class="body-copy">Options may include:</p>
      <ul class="options">
        <li>Acid Washed Concrete and a specialised Sealant applied to protect and enhance the concrete</li>
        <li>Concrete Grinding and Sealant applied with specific non slip beads</li>
        <li>Veltrex Terrazzo-Lite – decorative Flooring with Flake Finish – Seamless, safe &amp; waterproof</li>
        <li>Veltrex Grip-Coat – non slip flooring</li>
      </ul>
    </div>
    <div class="photo pool-photo" role="img" aria-label="Swimming pool with a pool house, tinted blue"></div>
  </section>

  <section class="panel panel-right">
    <div class="photo floor-photo" role="img" aria-label="Close-up of a speckled resin terrazzo floor beside a timber bench"></div>
    <div class="resin-title-band">
      <h2 class="heading">Resin Floors<br>and Floor<br>Toppings</h2>
    </div>
    <div class="resin-box">
      <p class="body-copy">TV Surfacing Contractors Limited are GOLD STAR Licensed Applicators of Veltrex Floor Toppings.</p>
      <p class="body-copy">Many industrial properties throughout New Zealand require well protected, non-slip hygienic floors in order to operate.</p>
      <p class="body-copy">As licensed applicators of Veltrex Terrazzo-Lite, Veltrex Glaze and Veltrex Grip etc., our team are the go-to call when you require superior floor toppings. Resin floor toppings are specialist systems that fully bond to the concrete, providing seamless, hard wearing and anti-microbial floors (which become durable and hygienic).</p>
      <p class="body-copy">Ideal in a variety of residential, commercial and industrial environments, resin floor toppings will help to meet any health and safety codes required by local authorities, and are becoming increasingly popular in homes given their practicality and aesthetic qualities.</p>
    </div>
  </section>

</main>
</body>
</html>
```